Clean, professional business cards for successful realtor

I want a clean and professional business card designed that successfully brands myself.
I want to be able to change the headshot, if possible. A white background instead of the brick would be great!
Please put this quote on the back of the card under the kiv logo, "Ask me about my Key-Turn program!"

Target Market(s)

Home buyers and sellers

Industry/Entity Type

Real Estate Agent

Contact Information for Business Card

Professional and Clean.

Font styles to use
Serif
Decorative
Script

Requirements
Must have
• Marisol Dunkel - Realtor
• Direct: 555.014.2298
• MariKeysSA@brightmailbox.net
• www.marisoldunkel.sa.kivhomesgroup.net
Nice to have
• Lighter colors, white and crisp would be nice.
• I would prefer my photo on the front of the card

```html
<!DOCTYPE html>
<html lang="en">
<head>
<meta charset="utf-8">
<title>Marisol Dunkel – Realtor Business Card</title>
<link rel="stylesheet" href="https://fonts.googleapis.com/css2?family=Montserrat:wght@400;500&family=Pacifico&family=Courgette&display=swap">
<style>
  :root {
    --teal: #0a9bb0;
    --white: #ffffff;
    --ink: #1e1e1e;
    --backdrop: #d6d6d6;
    --photo-warm: #9a7560;
    --photo-dark: #4a3530;
  }
  * { margin: 0; padding: 0; box-sizing: border-box; }
  html, body { width: 1200px; height: 1200px; overflow: hidden; }
  body {
    background: var(--backdrop);
    display: flex;
    flex-direction: column;
    align-items: center;
    justify-content: center;
    gap: 90px;
    font-family: "Montserrat", Arial, sans-serif;
  }
  .card {
    width: 700px;
    height: 400px;
    box-shadow: 0 14px 30px rgba(0,0,0,0.18);
    overflow: hidden;
  }
  .card-front { display: flex; background: var(--white); }
  .brand-column {
    width: 240px;
    flex-shrink: 0;
    background: var(--teal);
    display: flex;
    flex-direction: column;
    align-items: center;
    justify-content: center;
    gap: 44px;
  }
  .headshot {
    width: 160px;
    height: 160px;
    border-radius: 50%;
    border: 5px solid var(--white);
    background: radial-gradient(circle at 50% 45%, var(--photo-warm), var(--photo-dark));
  }
  .brand-mark {
    display: flex;
    align-items: center;
    gap: 10px;
    color: var(--white);
    font-family: "Montserrat", Arial, sans-serif;
    font-weight: 500;
    font-size: 34px;
    letter-spacing: 1px;
    line-height: 1;
  }
  .brand-dot {
    width: 16px;
    height: 16px;
    border-radius: 50%;
    background: var(--white);
  }
  .details {
    flex: 1;
    display: flex;
    flex-direction: column;
    justify-content: center;
    padding: 0 24px 0 36px;
    color: var(--ink);
  }
  .agent-name {
    font-family: "Pacifico", cursive;
    font-weight: 400;
    font-size: 48px;
    line-height: 1.2;
    margin-bottom: 4px;
  }
  .agent-title {
    font-size: 18px;
    letter-spacing: 1px;
    margin: 0 0 24px 90px;
  }
  .contact-line { font-size: 15px; line-height: 1.6; white-space: nowrap; }
  .card-back {
    background: var(--teal);
    display: flex;
    flex-direction: column;
    align-items: center;
    justify-content: center;
    gap: 26px;
    padding: 0 50px;
    color: var(--white);
    text-align: center;
  }
  .program-note {
    font-family: "Montserrat", Arial, sans-serif;
    font-size: 20px;
    font-weight: 500;
    letter-spacing: 0.5px;
  }
  .referral-quote {
    font-family: "Courgette", cursive;
    font-size: 23px;
    line-height: 1.4;
    max-width: 580px;
  }
</style>
</head>
<body>
  <section class="card card-front">
    <div class="brand-column">
      <div class="headshot" role="img" aria-label="Circular headshot of the realtor on a white background"></div>
      <div class="brand-mark"><span class="brand-dot"></span>kiv</div>
    </div>
    <div class="details">
      <h1 class="agent-name">Marisol Dunkel</h1>
      <p class="agent-title">REALTOR</p>
      <p class="contact-line">TEL. NO | 555.014.2298</p>
      <p class="contact-line">EMAIL | MariKeysSA@brightmailbox.net</p>
      <p class="contact-line">WEB | www.marisoldunkel.sa.kivhomesgroup.net</p>
    </div>
  </section>

  <section class="card card-back">
    <div class="brand-mark"><span class="brand-dot"></span>kiv</div>
    <p class="program-note">Ask me about my Key-Turn program!</p>
    <p class="referral-quote">" The referral of your family and friends is the greatest compliment you can give me, thank you for your trust."</p>
  </section>
</body>
</html>
```